Financial Service Company Need Business Card Design

This is a new startup company, first of its kind to offer this service. We facilitate the movement of deposit funds electronically between home buyers and real estate brokerages.Our customers are DOMIVANS®, real estate brokerages, and home buyers, we identify ourselves as a financial/technology company.
Not looking for anything too flashy. Just a clean design that shows the logo, contact info, etc. Company colors can be seen on attached logo, and 'coming soon page'
www.quorvanta.ca

```html
<!DOCTYPE html>
<html lang="en">
<head>
<meta charset="utf-8">
<title>Quorvanta Business Card</title>
<link rel="stylesheet" href="https://fonts.googleapis.com/css2?family=Cinzel:wght@400;700&display=swap">
<style>
  :root {
    --page-bg: #e6e6e6;
    --card-white: #f7f7f5;
    --brand-orange: #e4532b;
    --brand-orange-light: #ea6a3c;
    --brand-grey: #58595b;
    --card-dark-top: #6a6b6d;
    --card-dark-bottom: #4d4e50;
    --ink: #4a4a4a;
    --rule: #5a5a5a;
    --white: #ffffff;
  }
  * { margin: 0; padding: 0; box-sizing: border-box; }
  html, body {
    width: 1200px; height: 720px; overflow: hidden;
    background: var(--page-bg);
    font-family: "Cinzel", Georgia, serif;
  }
  .canvas { position: relative; width: 1200px; height: 720px; }
  .card {
    position: absolute; top: 241px; width: 420px; height: 240px; overflow: hidden;
  }
  .card--front { left: 147px; background: var(--card-white); }
  .card--back {
    left: 633px;
    background: linear-gradient(160deg, var(--card-dark-top), var(--card-dark-bottom));
    display: flex; align-items: center; justify-content: center;
  }
  .brand { display: flex; align-items: center; gap: 9px; }
  .brand__mark { width: 26px; height: 26px; background: var(--brand-orange); }
  .brand__name { font-weight: 700; font-size: 27px; line-height: 1; color: var(--brand-grey); }
  .card--front .brand { position: absolute; left: 26px; top: 29px; }
  .card--back .brand__mark { width: 38px; height: 38px; background: var(--white); }
  .card--back .brand__name { font-size: 40px; color: var(--white); }
  .card--back .brand { gap: 12px; }
  .holder { position: absolute; right: 27px; top: 84px; text-align: right; }
  .holder__name { font-weight: 700; font-size: 13px; color: var(--brand-orange); line-height: 1.1; }
  .holder__role { font-size: 9.5px; color: var(--ink); line-height: 1.2; }
  .divider { position: absolute; left: 26px; right: 27px; top: 124px; height: 1.5px; background: var(--rule); }
  .contacts { position: absolute; left: 26px; top: 142px; list-style: none; }
  .contacts li {
    display: flex; align-items: center; gap: 6px;
    font-size: 9.5px; color: var(--ink); line-height: 12.3px;
  }
  .contacts svg { width: 9px; height: 9px; fill: var(--brand-orange); flex: none; }
  .address {
    position: absolute; right: 27px; top: 138px; text-align: right;
    font-size: 9.5px; color: var(--ink); line-height: 12.3px;
  }
  .accent-band {
    position: absolute; left: 0; right: 0; bottom: 0; height: 40px;
    background: linear-gradient(90deg, var(--brand-orange), var(--brand-orange-light));
  }
</style>
</head>
<body>
<main class="canvas">
  <section class="card card--front" aria-label="Business card front">
    <div class="brand">
      <span class="brand__mark"></span>
      <span class="brand__name">Quorvanta</span>
    </div>
    <div class="holder">
      <p class="holder__name">Marlo Venn</p>
      <p class="holder__role">Manager</p>
    </div>
    <div class="divider"></div>
    <ul class="contacts">
      <li><svg viewBox="0 0 10 10"><path d="M1 3 Q5 0 9 3 L8 4.5 L6.5 3.8 L6.5 3 Q5 2.6 3.5 3 L3.5 3.8 L2 4.5 Z M2.5 5 H7.5 L8.5 9 H1.5 Z"/></svg>604 555 0182</li>
      <li><svg viewBox="0 0 10 10"><path d="M3 0.5 H7 V9.5 H3 Z M3.8 1.5 V7.8 H6.2 V1.5 Z"/></svg>+1 604 555 0147</li>
      <li><svg viewBox="0 0 10 10"><path d="M0.5 2 H9.5 V8 H0.5 Z M1.3 2.6 L5 5.4 L8.7 2.6 Z"/></svg>info@quorvanta.ca</li>
      <li><svg viewBox="0 0 10 10"><path d="M0.5 1.5 H9.5 V7 H0.5 Z M1.4 2.3 V6.2 H8.6 V2.3 Z M3.5 8 H6.5 V9 H3.5 Z"/></svg>www.quorvanta.ca</li>
    </ul>
    <p class="address">Here your company or<br>home address</p>
    <div class="accent-band" role="img" aria-label="Decorative orange and grey wave band along the bottom edge"></div>
  </section>

  <section class="card card--back" aria-label="Business card back">
    <div class="brand">
      <span class="brand__mark"></span>
      <span class="brand__name">Quorvanta</span>
    </div>
  </section>
</main>
</body>
</html>
```